Business Card Design - Carrington Hill Lodge

We are looking at a new design for our business cards that has a modern and professional look. We run a residential aged care facility focussing on the care of residents. The cards will be used for potential clients, consultants and business opportunities in this sector. Blue and white is our main colours and would to see these colours incorporated in the design.
Industry/Entity Type
Business
Contact Information for Business Card
Carrington Hill Lodge, Darren Pelham, dpelham@carringtonhilllodge.com.au, Finance Manager, 0491 736 208, BCom, 48 Yarrabee Way, Bellmere Park, Qld 4119.

```html
<!DOCTYPE html>
<html lang="en">
<head>
<meta charset="utf-8">
<title>Carrington Hill Lodge – Business Card</title>
<link rel="stylesheet" href="https://fonts.googleapis.com/css2?family=Oswald:wght@300;400&family=PT+Sans:ital,wght@0,400;1,400&display=swap">
<style>
  :root {
    --page-bg: #dcd8d3;
    --card-bg: #ffffff;
    --brand-blue: #4d7a96;
    --brand-navy: #1f3447;
    --taupe: #a99c94;
    --ink: #333333;
    --rule: #9a9a9a;
  }
  * { margin: 0; padding: 0; box-sizing: border-box; }
  html, body { width: 1200px; height: 1000px; overflow: hidden; }
  body { background: var(--page-bg); position: relative; font-family: "PT Sans", sans-serif; }

  .card {
    position: absolute; left: 236px; width: 728px; height: 415px;
    background: var(--card-bg); overflow: hidden;
    box-shadow: 0 4px 14px rgba(0,0,0,0.25);
  }
  .card--front { top: 72px; }
  .card--back { top: 512px; }

  .card__base { position: absolute; left: 0; top: 0; width: 728px; height: 415px; }

  .brand { position: absolute; text-align: center; }
  .brand__name {
    font-family: "Oswald", sans-serif; font-weight: 300;
    color: var(--brand-navy); letter-spacing: 2px; text-transform: uppercase;
    white-space: nowrap; line-height: 1;
  }
  .brand__tagline {
    display: inline-block; color: var(--taupe);
    font-family: "PT Sans", sans-serif; font-style: italic; white-space: nowrap;
    border-top: 1px solid var(--taupe);
  }

  .card--front .brand { left: 0; width: 728px; top: 214px; }
  .card--front .brand__name { font-size: 38px; }
  .card--front .brand__tagline { margin-top: 12px; padding: 6px 24px 0; font-size: 19px; line-height: 24px; }

  .card--back .brand { left: 40px; width: 320px; top: 214px; }
  .card--back .brand__name { font-size: 25px; }
  .card--back .brand__tagline { margin-top: 9px; padding: 5px 18px 0; font-size: 15px; line-height: 19px; }

  .website-link {
    position: absolute; right: 34px; top: 374px;
    color: #fff; font-style: italic; font-size: 15px;
  }

  .contact { position: absolute; left: 381px; top: 86px; color: var(--ink); }
  .contact__name {
    font-family: "Oswald", sans-serif; font-weight: 400; font-size: 21px;
    color: var(--brand-blue); text-transform: uppercase; letter-spacing: 0.5px; line-height: 1.2;
  }
  .contact__role { font-size: 15px; margin-top: 2px; }
  .contact__rule {
    width: 80px; height: 1px; margin: 10px 0 12px;
    background: linear-gradient(to right, var(--rule), rgba(154,154,154,0));
  }
  .contact__address { font-size: 15px; line-height: 21px; }
  .contact__list { list-style: none; margin-top: 11px; font-size: 15px; line-height: 23px; }
  .contact__list li { display: flex; align-items: center; gap: 7px; }
  .contact__icon { width: 12px; height: 12px; flex: none; fill: var(--brand-blue); }
</style>
</head>
<body>

<section class="card card--front">
  <svg class="card__base" viewBox="0 0 728 415" aria-hidden="true">
    <path d="M0,370 C200,372 480,350 728,300" fill="none" stroke="var(--taupe)" stroke-width="3"/>
    <path d="M0,380 C200,384 480,362 728,312 L728,415 L0,415 Z" fill="var(--brand-blue)"/>
  </svg>
  <div class="brand">
    <div class="brand__name">Carrington Hill Lodge</div>
    <span class="brand__tagline">Care, Comfort, Community</span>
  </div>
  <span class="website-link">www.carringtonhilllodge.com.au</span>
</section>

<section class="card card--back">
  <svg class="card__base" viewBox="0 0 728 415" aria-hidden="true">
    <path d="M0,370 C200,372 480,350 728,300" fill="none" stroke="var(--taupe)" stroke-width="3"/>
    <path d="M0,380 C200,384 480,362 728,312 L728,415 L0,415 Z" fill="var(--brand-blue)"/>
  </svg>
  <div class="brand">
    <div class="brand__name">Carrington Hill Lodge</div>
    <span class="brand__tagline">Care, Comfort, Community</span>
  </div>
  <div class="contact">
    <div class="contact__name">Darren Pelham</div>
    <div class="contact__role">Finance Manager</div>
    <div class="contact__rule"></div>
    <div class="contact__address">48 Yarrabee Way,<br>Bellmere Park, Qld 4119</div>
    <ul class="contact__list">
      <li>
        <svg class="contact__icon" viewBox="0 0 24 24" aria-hidden="true"><path d="M6.6 10.8a15.1 15.1 0 0 0 6.6 6.6l2.2-2.2a1 1 0 0 1 1-.25 11.4 11.4 0 0 0 3.6.57 1 1 0 0 1 1 1V20a1 1 0 0 1-1 1A17 17 0 0 1 3 4a1 1 0 0 1 1-1h3.5a1 1 0 0 1 1 1c0 1.25.2 2.45.57 3.6a1 1 0 0 1-.25 1z"/></svg>
        0491 736 208
      </li>
      <li>
        <svg class="contact__icon" viewBox="0 0 24 24" aria-hidden="true"><path d="M2 5h20v14H2z M2 5l10 8 10-8" fill="var(--brand-blue)" stroke="#fff" stroke-width="1.5"/></svg>
        dpelham@carringtonhilllodge.com.au
      </li>
      <li>
        <svg class="contact__icon" viewBox="0 0 24 24" aria-hidden="true"><g fill="none" stroke="var(--brand-blue)" stroke-width="2"><circle cx="12" cy="12" r="10"/><ellipse cx="12" cy="12" rx="4.5" ry="10"/><path d="M2 12h20"/></g></svg>
        www.carringtonhilllodge.com.au
      </li>
    </ul>
  </div>
</section>

</body>
</html>
```